Poster for a Bicycle show/Expo

We need a poster for a Bicycle show/Expo and sustainable transport. Exhibitors will sell bikes, cycling clothing, accessories, etc. ...
This show is annual and the Poster is for the 2016 edition.

Your concept must be compatible in a landscape format. (We will ourselves adaptations of different formats.)
Width: 210 mm
Height: 297 mm
It's necessary for us to have the source file (vector) for make, later, the different format (flyers, website, ...)

Content of the Poster:
- 1 big picture (one of the two attached)
- Big title (typo-title worked): « Foire du Rouet » (« Salon » or « Salon du » can be small and « Vélo » big.)
- Subtitle: « et de la mobilité durable »
- Date: « 18, 19 et 20 mars 2016 » or « 18-20 mars 2016 »
- Place: « Halle RTP - Gare de Plantaz »
- Text line 1: « www.foire-du-rouet.ch »
- Text line 2: « Entrée gratuite »
- Text line 3: « Ve 18 mars de 17h à 20h - Sa 19 mars de 10h à 18h - Di 20 mars de 10h à 17h »
- Please, leave a zone in the poster for sponsors logos
(The predominant information (most visible) are: « Vélo » and « 18, 19 et 20 mars 2016 » or « 18-20 mars 2016 »)

Target Market(s)

Bicycle fan

Industry/Entity Type

Sporting Good

Font styles to use
Serif
Sans Serif

Colors
add136
ffffff
ec1f27

Requirements
Must have
• The style must be modern, dynamic, bright colors.

```html
<!DOCTYPE html>
<html lang="fr">
<head>
<meta charset="utf-8">
<title>Foire du Rouet 2016</title>
<link href="https://fonts.googleapis.com/css2?family=Michroma&display=swap" rel="stylesheet">
<style>
  :root {
    --magenta: #e4127e;
    --ink: #2a2a2a;
    --red: #ec1f27;
    --sky-top: #1f8fe0;
    --sky-mid: #8ec6ee;
    --cloud: #e9eef2;
    --cloud-grey: #b9c0c6;
    --grass-light: #add136;
    --grass-dark: #4f8a1c;
    --white: #ffffff;
  }
  html, body {
    margin: 0;
    padding: 0;
    overflow: hidden;
  }
  .poster {
    position: relative;
    width: 849px;
    height: 1200px;
    overflow: hidden;
    font-family: "Michroma", "Arial", sans-serif;
    background: var(--white);
  }
  .backdrop {
    position: absolute;
    inset: 0;
    background:
      linear-gradient(180deg,
        var(--sky-top) 0%,
        var(--sky-mid) 18%,
        var(--cloud) 32%,
        var(--cloud-grey) 52%,
        var(--cloud) 70%,
        var(--white) 77%,
        var(--grass-light) 80%,
        var(--grass-dark) 100%);
  }
  .bike-sketch {
    position: absolute;
    left: 60px;
    top: 30px;
    width: 620px;
    height: 240px;
    border-radius: 120px;
    background: radial-gradient(ellipse at center, rgba(255,255,255,0.55) 0%, rgba(255,255,255,0) 70%);
  }
  .rider {
    position: absolute;
    left: 566px;
    top: 470px;
    width: 283px;
    height: 540px;
    border-radius: 140px 0 0 40px;
    background: linear-gradient(180deg, rgba(90,90,95,0.55) 0%, rgba(40,40,45,0.7) 100%);
  }
  .title {
    position: absolute;
    left: 0;
    right: 0;
    top: 262px;
    margin: 0;
    text-align: center;
    color: var(--magenta);
    font-weight: 400;
    font-size: 62px;
    font-variant: small-caps;
    letter-spacing: 2px;
    line-height: 1;
  }
  .subtitle {
    position: absolute;
    left: 0;
    right: 0;
    top: 350px;
    text-align: center;
    color: var(--ink);
    font-size: 22px;
    text-transform: uppercase;
    letter-spacing: 1px;
  }
  .date {
    position: absolute;
    left: 0;
    right: 0;
    top: 472px;
    text-align: center;
    color: var(--magenta);
    font-size: 60px;
    font-variant: small-caps;
    letter-spacing: 1px;
    line-height: 1;
  }
  .venue {
    position: absolute;
    left: 0;
    right: 0;
    top: 580px;
    text-align: center;
    color: var(--ink);
    font-size: 30px;
    font-variant: small-caps;
  }
  .entry {
    position: absolute;
    left: 0;
    right: 0;
    top: 630px;
    text-align: center;
    color: var(--ink);
    font-size: 12px;
    text-transform: uppercase;
    letter-spacing: 1px;
  }
  .hours {
    position: absolute;
    left: 0;
    right: 0;
    top: 664px;
    text-align: center;
    color: var(--red);
    font-size: 9px;
    text-transform: uppercase;
  }
  .website {
    position: absolute;
    left: 70px;
    top: 840px;
    color: var(--magenta);
    font-size: 16px;
    text-transform: uppercase;
    letter-spacing: 1px;
  }
  .sponsors {
    position: absolute;
    left: 42px;
    top: 1146px;
    width: 86px;
    height: 38px;
    background: var(--white);
    border: 1px solid var(--cloud-grey);
    display: flex;
    align-items: center;
    justify-content: center;
    font-size: 6px;
    color: var(--ink);
    text-transform: uppercase;
  }
</style>
</head>
<body>
  <main class="poster">
    <div class="backdrop" role="img" aria-label="Photo: ciel bleu avec nuages gris au-dessus d'une prairie verte"></div>
    <div class="bike-sketch" role="img" aria-label="Dessin à la craie d'un vélo dans le ciel"></div>
    <div class="rider" role="img" aria-label="Photo: une cycliste sur un VTT dans la prairie"></div>

    <h1 class="title">Foire du Rouet</h1>
    <div class="subtitle">et de la mobilité durable</div>
    <div class="date">18-20 mars 2016</div>
    <div class="venue">Halle RTP - Gare de Plantaz</div>
    <div class="entry">Entrée gratuite</div>
    <div class="hours">Ve 18 mars de 17h à 20h - Sa 19 mars de 10h à 18h - Di 20 mars de 10h à 17h</div>
    <div class="website">www.foire-du-rouet.ch</div>
    <div class="sponsors">Sponsors</div>
  </main>
</body>
</html>
```